website for local kavenda practicioner and yoga teacher trainer

The website should function primarily as:
A place where people can discover Kavenda and book sessions.
A central hub connecting all of my work.
A professional home that reflects my personality and approach.
Website design for Liesbet Oonwerk — Kavenda® Structural Integration practitioner, movement educator, yoga teacher and teacher trainer.
A website that can grow with future projects.
The website should feel: Warm, Human, Invitational, Professional, Accessible, Intelligent, Calm, Clear, Playful, Exploratory, Trustworthy
Avoid: New age aesthetics, Mystical clichés, Excessive spirituality, ”Guru" vibes, Overly clinical design, Corporate wellness branding, Busy layouts
Think: modern, grounded, curious and real.
My work combines three interconnected areas:
1.Bodywork: Touch, structure, awareness and one-on-one support.
2. Movement: Yoga, Pilates and embodied movement.
3. Education: Teacher trainings, workshops and continued learning.
Underlying values:
Curiosity over certainty
Possibility over perfection
Complexity without overwhelm
Science and lived experience together
Exploration rather than dogma
Human beings before methods
The primary goal of the website is to introduce people to Kavenda® Structural Integration and make it easy for them to:
Understand what Kavenda is
Discover whether it might be relevant for them
Learn what to expect from a session
Book an appointment
Booking should always feel visible and easy.
Secondary Goal: Present all other aspects of my work in one coherent place:
Yoga classes
Pilates classes
Teacher trainings
Workshops
Retreats
One-on-one movement sessions
Collaborations with studios
Website Structure
1: HOME
1.1.Hero Section: Large welcoming image
1.2 Two Main Pathways
- Bodywork: Kavenda® Structural Integration
- Movement & Education: Yoga, Pilates, trainings, workshops and retreats
- About Preview: Small introduction with portrait. + Button:
Read More
1.3 Current Events / What's Coming Up: Upcoming trainings, workshops and retreats. (This section should be easy to update)
1.4. Contact / Newsletter: Simple contact information
2: Kavenda® Structural Integration
What is Kavenda?
For whom is it?
What does a session look like?
FAQ
Prices
Booking
Future possibility:
Kaven Movement sessions
3: Movement
- Introductory text.
- Studio Classes (link to “my home base” - > local yoga studio)
- One-to-One Sessions: booking option (this is small; not a key aspect I want to promote)
- Workshops/ Retreats / Teacher Trainings => This section should be flexible and easy to update. Visitors should be able to click into specific offerings.
4. Events
Dynamic page for: Teacher trainings, Retreats, Workshops (see section in movement; here more elaborate)
Each event should contain: Image, Short description, Location, Date, Button for more information. (Linking to hosting studio/location)
5. Work With Me
For studios, organisations and teacher training schools.
Examples: Guest teaching, Workshops, Anatomy, Sequencing, Teacher development , Continuing education -> Clear call-to-action.
Call to action!!=> Book a Session
Prominent button in the navigation.
Footer:
- About Me: Longer biography (6th page)
Personal story and background.
- Testimonials (7th page): Separate page containing testimonials from:
Kavenda clients
Students
Teacher trainees
- Contact: 8th page
Visual Direction
Natural textures. Lots of white space.Editorial feeling.Professional photography.Simple navigation.
Less "wellness influencer.” More:Thoughtful, Contemporary, Timeless, Grounded, Human
Photography should show:
Teaching
Hands-on work
Natural movement
Real interaction
Simplicity
Avoid stereotypical yoga imagery and overly spiritual aesthetics.
Keywords
Warm. Curious. Human. Professional. Embodied. Intelligent. Accessible. Playful. Grounded. Exploratory. Real.
Inspiration / Core Message
Helping people feel more at home in their bodies through touch, movement and education.
The website should communicate that these are not separate services, but different expressions of the same intention:
Bodywork • Movement • Education.
Colours:
light orange/beige: e3d5c4
light orange/off white: f9f7f3
gray azure: 556b78
orange: d07b5a
grey orange: c09f80
dark grey: 3e3e3e
dark gray cyan 2f4f4f
gray green colour: a7c4a0
Fonts: Montserrat and Poppins + raleway
In added documents a try out idea of a website + logo. I will mainly use the logo with diffrent colours (image next to text).
My audience consists of people who want to feel more at home in their bodies and who appreciate a thoughtful, grounded and human approach to movement, touch and education. (30-65yo)
wellbeing
5+ page
- montserrat, poppins, raleway

```html
<!DOCTYPE html>
<html lang="en">
<head>
<meta charset="utf-8">
<title>Liesbet Oonwerk — Yoga & Bodywork</title>
<link rel="stylesheet" href="https://fonts.googleapis.com/css2?family=Poppins:ital,wght@0,300;0,400;0,500;0,600;1,300;1,400&family=Montserrat:wght@400;500;600&display=swap">
<style>
:root{
  --sand:#e3d5c4;
  --offwhite:#f9f7f3;
  --cream:#f5f2ed;
  --azure:#556b78;
  --azure-dark:#465a66;
  --orange:#c9694a;
  --orange-soft:#d07b5a;
  --peach:#efd6cb;
  --greyorange:#c09f80;
  --charcoal:#3e3e3e;
  --cyan:#2f4f4f;
  --green:#a7c4a0;
  --text:#2b2b2b;
  --muted:#5a5a5a;
  --white:#fff;
}
*{box-sizing:border-box;margin:0;padding:0}
html,body{width:1200px;height:4662px;overflow:hidden}
body{font-family:"Poppins",sans-serif;color:var(--text);background:var(--white);position:relative}
section,header,footer{position:relative;width:1200px;overflow:hidden}
.abs{position:absolute}
.eyebrow{font-family:"Montserrat",sans-serif;font-size:15px;letter-spacing:3px;text-transform:uppercase;font-weight:500}
.hl{background:var(--orange);color:var(--white);font-style:italic;font-weight:300;padding:0 6px}
.link{color:var(--orange);font-size:16px;font-weight:500;text-decoration:none;display:inline-flex;align-items:center;gap:8px}
.btn{display:inline-flex;align-items:center;justify-content:center;font-weight:600;font-size:16px;border-radius:3px;text-decoration:none}
.btn-primary{background:var(--orange);color:var(--white)}

/* Header */
.site-header{height:110px;background:var(--offwhite)}
.brand{left:52px;top:36px;display:flex;align-items:center;gap:12px}
.brand-dot{width:30px;height:30px;border-radius:50%;background:var(--orange)}
.brand-name{font-size:25px;font-weight:400;color:var(--charcoal)}
.main-nav{left:388px;top:44px;display:flex;gap:20px;font-size:16px;font-weight:500}
.main-nav a{color:var(--text);text-decoration:none}
.main-nav a.active{color:var(--orange)}
.nav-cta{left:938px;top:29px;width:191px;height:51px}

/* Hero */
.hero{height:681px;background:var(--charcoal)}
.hero-photo{left:430px;top:0;width:800px;height:681px;border-radius:260px 0 0 0/681px 0 0 0;background:linear-gradient(135deg,#8a6a58 0%,#b89680 35%,#7c8c94 75%,#5f7079 100%)}
.hero-eyebrow{left:109px;top:121px;color:var(--orange-soft)}
.hero-title{left:109px;top:150px;font-size:68px;line-height:83px;font-weight:400;color:var(--white)}
.hero-text{left:109px;top:418px;width:440px;font-size:16px;line-height:25px;color:#eee}
.hero-actions{left:109px;top:511px;display:flex;gap:25px}
.hero-actions .btn{height:51px}
.btn-ghost{border:1.5px solid var(--white);color:var(--white)}

/* Offer */
.offer{height:1186px;background:var(--offwhite)}
.center{left:0;width:1200px;text-align:center}
.offer-eyebrow{top:120px;color:var(--azure)}
.section-title{font-size:45px;line-height:51px;font-weight:300;color:var(--text)}
.offer-title{top:150px}
.offer-sub{top:258px;font-size:16px;line-height:26px;color:var(--muted)}
.path-card{top:347px;width:483px;height:623px;background:var(--white);border-radius:4px;box-shadow:0 2px 8px rgba(0,0,0,.12)}
.path-photo{width:483px;height:384px;border-radius:4px 4px 0 0}
.path-body{padding:28px 27px}
.path-body .eyebrow{color:var(--orange);font-size:15px}
.path-body h3{font-size:18px;font-weight:400;margin:20px 0 18px}
.path-body p{font-size:14px;line-height:23px;color:var(--muted);margin-bottom:18px}
.quote{top:1030px;font-size:43px;font-weight:300;color:var(--azure)}
.quote-by{top:1096px;color:var(--orange);font-size:15px}

/* About */
.about{height:794px;background:var(--white)}
.about-eyebrow{left:109px;top:211px;color:var(--cyan)}
.about-title{left:109px;top:244px;font-size:45px;line-height:50px;font-weight:300}
.about-text{left:109px;top:420px;width:460px;font-size:16px;line-height:25px;color:var(--muted)}
.about-more{left:109px;top:558px}
.accent-a{left:802px;top:124px;width:308px;height:145px;background:var(--peach);border-radius:8px}
.accent-b{left:594px;top:513px;width:309px;height:140px;background:var(--peach);border-radius:8px}
.about-photo{left:608px;top:139px;width:483px;height:501px;border-radius:4px;background:linear-gradient(160deg,#cfc5b8 0%,#8e7a66 45%,#3b3733 80%,#6d8a5f 100%)}

/* Events */
.events{height:894px;background:var(--cream)}
.events-eyebrow{left:109px;top:101px;color:var(--cyan)}
.events-title{left:109px;top:136px}
.events-all{left:950px;top:171px;font-size:15px}
.event-card{top:281px;width:316px;height:465px;background:var(--white);border:1px solid #e3e0db;border-radius:4px;overflow:hidden}
.event-photo{height:200px}
.event-body{padding:38px 20px 0}
.tag{display:inline-block;font-family:"Montserrat",sans-serif;font-size:11px;letter-spacing:2px;text-transform:uppercase;padding:4px 12px;border-radius:12px}
.tag-retreat{background:#e4eee1;color:#4c6d46}
.tag-training{background:#f1ddd1;color:var(--orange)}
.event-body h3{font-size:18px;font-weight:400;color:var(--text);line-height:26px;margin:14px 0 16px}
.meta{display:flex;align-items:center;gap:8px;font-size:11px;color:var(--muted);margin-bottom:12px}
.event-more{font-size:16px;color:var(--text);display:inline-flex;align-items:center;gap:8px;margin-top:10px}
.training h3{color:var(--orange);margin-top:6px}

/* Connect */
.connect{height:666px;background:var(--white)}
.connect-card{top:112px;width:483px;height:448px;border-radius:6px;padding:72px 36px 0}
.booking{left:109px;background:var(--azure-dark);color:var(--white)}
.newsletter{left:608px;background:var(--cream);border:1px solid #ddd}
.connect-card .eyebrow{font-size:15px}
.booking .eyebrow{color:#e9e9e9}
.newsletter .eyebrow{color:var(--orange)}
.connect-card h2{font-size:45px;line-height:50px;font-weight:300;margin:16px 0 14px}
.connect-card p{font-size:16px;line-height:25px}
.booking p{color:#eee}
.newsletter p{color:var(--muted)}
.booking .btn{width:192px;height:52px;margin-top:40px}
.email-field{margin-top:16px;height:49px;border:1px solid #e1ddd6;background:var(--white);font-size:15px;color:#999;padding:0 14px;display:flex;align-items:center}
.newsletter .btn{width:100%;height:51px;margin-top:12px}

/* Footer */
.site-footer{height:331px;background:var(--sand)}
.footer-brand{left:109px;top:92px;display:flex;align-items:center;gap:12px}
.footer-brand .brand-name{font-size:30px}
.footer-tag{left:109px;top:170px;width:270px;font-size:12px;line-height:17px;color:var(--charcoal)}
.fcol{top:67px}
.fcol h4{font-size:15px;font-weight:600;color:var(--orange);margin-bottom:14px}
.fcol a{display:block;font-size:14px;color:var(--text);text-decoration:none;margin-bottom:13px}
.contact-item{display:flex;gap:12px;font-size:14px;line-height:21px;margin-bottom:14px;width:230px}
.footer-base{left:109px;top:306px;width:982px;display:flex;justify-content:space-between;font-size:12px;color:var(--charcoal)}
</style>
</head>
<body>

<header class="site-header">
  <div class="abs brand"><span class="brand-dot"></span><span class="brand-name">Liesbet Oonwerk</span></div>
  <nav class="abs main-nav">
    <a class="active" href="#">Home</a><a href="#">Kavenda</a><a href="#">Movement</a><a href="#">Events</a><a href="#">Work With Me</a>
  </nav>
  <a class="abs btn btn-primary nav-cta" href="#">Book A Session</a>
</header>

<section class="hero">
  <div class="abs hero-photo" role="img" aria-label="Hands of a practitioner working on a client's shoulder and back"></div>
  <p class="abs eyebrow hero-eyebrow">Yoga &amp; Bodywork</p>
  <h1 class="abs hero-title">Helping you feel<br>more <span class="hl">at home</span><br>in your body</h1>
  <p class="abs hero-text">Through Kavenda Structural Integration, yoga, and embodied movement education. Curiosity over certainty. Possibility over perfection.</p>
  <div class="abs hero-actions">
    <a class="btn btn-primary" href="#" style="width:190px">Discover Kavenda</a>
    <a class="btn btn-ghost" href="#" style="width:190px">Explore Movement</a>
  </div>
</section>

<section class="offer">
  <p class="abs center eyebrow offer-eyebrow">What I Offer</p>
  <h2 class="abs center section-title offer-title">Three Expressions of<br>the Same <span class="hl">Intention</span></h2>
  <p class="abs center offer-sub">Bodywork, Movement, and Education — different ways of supporting you<br>to reconnect with your body's natural intelligence.</p>

  <article class="abs path-card" style="left:109px">
    <div class="path-photo" role="img" aria-label="Hands working on a client's back in warm striped sunlight" style="background:linear-gradient(140deg,#e8e2d8 0%,#c07a48 45%,#8a4b26 100%)"></div>
    <div class="path-body">
      <p class="eyebrow">Bodywork</p>
      <h3>Kavenda® Structural Integration</h3>
      <p>A collaborative process exploring posture, movement, breath, and relationship to gravity through touch, awareness, and movement...</p>
      <a class="link" href="#">Learn More <svg width="12" height="12" viewBox="0 0 12 12"><path d="M1 6h9M6 2l4 4-4 4" stroke="currentColor" stroke-width="1.6" fill="none"/></svg></a>
    </div>
  </article>

  <article class="abs path-card" style="left:608px">
    <div class="path-photo" role="img" aria-label="Group class stretching seated on mats in a bright studio" style="background:linear-gradient(160deg,#d9d6d0 0%,#9a958d 50%,#4f6a80 100%)"></div>
    <div class="path-body">
      <p class="eyebrow">Movement &amp; Education</p>
      <h3>Yoga, Pilates, trainings, workshops and retreats</h3>
      <p>Movement as exploration — a space to build strength, mobility, awareness, and resilience. From group classes and private sessions to teacher trainings...</p>
      <a class="link" href="#">Learn More <svg width="12" height="12" viewBox="0 0 12 12"><path d="M1 6h9M6 2l4 4-4 4" stroke="currentColor" stroke-width="1.6" fill="none"/></svg></a>
    </div>
  </article>

  <blockquote class="abs center quote">"Bodies are plastic to the intent of life."</blockquote>
  <p class="abs center eyebrow quote-by">— Ilse Varden</p>
</section>

<section class="about">
  <p class="abs eyebrow about-eyebrow">About Liesbet</p>
  <h2 class="abs about-title"><span class="hl">Curiosity shapes</span> how<br>I move, teach, touch,<br>and relate to people</h2>
  <p class="abs about-text">What connects my work is curiosity: the body is not something to perfect or control, but something to listen to, explore, and live within. Every body carries stories, habits, tensions, and possibilities — and every story moves.</p>
  <a class="abs link about-more" href="#">Read More <svg width="12" height="12" viewBox="0 0 12 12"><path d="M1 6h9M6 2l4 4-4 4" stroke="currentColor" stroke-width="1.6" fill="none"/></svg></a>
  <div class="abs accent-a"></div>
  <div class="abs accent-b"></div>
  <div class="abs about-photo" role="img" aria-label="Portrait of Liesbet seated in an armchair in a bright practice room, holding a tablet"></div>
</section>

<section class="events">
  <p class="abs eyebrow events-eyebrow">What's Coming Up</p>
  <h2 class="abs section-title events-title">Upcoming <span class="hl">Events</span></h2>
  <a class="abs link events-all" href="#">View All Events <svg width="12" height="12" viewBox="0 0 12 12"><path d="M1 6h9M6 2l4 4-4 4" stroke="currentColor" stroke-width="1.6" fill="none"/></svg></a>

  <article class="abs event-card" style="left:109px">
    <div class="event-photo" role="img" aria-label="Person sitting on a hillside looking over misty mountains" style="background:linear-gradient(180deg,#c9cdd0 0%,#8d949a 55%,#4b4e44 100%)"></div>
    <div class="event-body">
      <span class="tag tag-retreat">Retreat</span>
      <h3>Spring Movement Retreat</h3>
      <div class="meta"><svg width="14" height="14" viewBox="0 0 14 14" fill="none" stroke="#c9694a" stroke-width="1.2"><rect x="1.5" y="2.5" width="11" height="10" rx="1"/><path d="M1.5 5.5h11M4.5 1v3M9.5 1v3"/></svg>15–17 March 2025</div>
      <div class="meta"><svg width="14" height="14" viewBox="0 0 14 14" fill="none" stroke="#c9694a" stroke-width="1.3"><path d="M7 13s4.5-4.2 4.5-7.5a4.5 4.5 0 0 0-9 0C2.5 8.8 7 13 7 13z"/><circle cx="7" cy="5.5" r="1.6"/></svg>Dordogne, France</div>
      <span class="event-more">More Information <svg width="12" height="12" viewBox="0 0 12 12"><path d="M1 6h9M6 2l4 4-4 4" stroke="currentColor" stroke-width="1.6" fill="none"/></svg></span>
    </div>
  </article>

  <article class="abs event-card training" style="left:442px">
    <div class="event-photo" role="img" aria-label="Teacher standing in front of students seated cross-legged on mats" style="background:linear-gradient(180deg,#e6e2dc 0%,#b5aa9c 55%,#6a5a4c 100%)"></div>
    <div class="event-body" style="padding-top:38px">
      <span class="tag tag-training">Training</span>
      <h3>200-Hour Yoga Teacher<br>Training</h3>
      <div class="meta"><svg width="14" height="14" viewBox="0 0 14 14" fill="none" stroke="#c9694a" stroke-width="1.2"><rect x="1.5" y="2.5" width="11" height="10" rx="1"/><path d="M1.5 5.5h11M4.5 1v3M9.5 1v3"/></svg>September 2025 – July 2026</div>
      <div class="meta"><svg width="14" height="14" viewBox="0 0 14 14" fill="none" stroke="#c9694a" stroke-width="1.3"><path d="M7 13s4.5-4.2 4.5-7.5a4.5 4.5 0 0 0-9 0C2.5 8.8 7 13 7 13z"/><circle cx="7" cy="5.5" r="1.6"/></svg>Leiden, The Netherlands</div>
      <span class="event-more">More Information <svg width="12" height="12" viewBox="0 0 12 12"><path d="M1 6h9M6 2l4 4-4 4" stroke="currentColor" stroke-width="1.6" fill="none"/></svg></span>
    </div>
  </article>

  <article class="abs event-card" style="left:775px">
    <div class="event-photo" role="img" aria-label="Small group sitting on a beach at sunset with palm trees" style="background:linear-gradient(180deg,#5e6f8c 0%,#c48a6a 50%,#e6b07a 62%,#5a4a44 100%)"></div>
    <div class="event-body">
      <span class="tag tag-retreat">Retreat</span>
      <h3>Autumn Embodiment Retreat</h3>
      <div class="meta"><svg width="14" height="14" viewBox="0 0 14 14" fill="none" stroke="#c9694a" stroke-width="1.2"><rect x="1.5" y="2.5" width="11" height="10" rx="1"/><path d="M1.5 5.5h11M4.5 1v3M9.5 1v3"/></svg>10–12 October 2025</div>
      <div class="meta"><svg width="14" height="14" viewBox="0 0 14 14" fill="none" stroke="#c9694a" stroke-width="1.3"><path d="M7 13s4.5-4.2 4.5-7.5a4.5 4.5 0 0 0-9 0C2.5 8.8 7 13 7 13z"/><circle cx="7" cy="5.5" r="1.6"/></svg>Belgium</div>
      <span class="event-more">More Information <svg width="12" height="12" viewBox="0 0 12 12"><path d="M1 6h9M6 2l4 4-4 4" stroke="currentColor" stroke-width="1.6" fill="none"/></svg></span>
    </div>
  </article>
</section>

<section class="connect">
  <div class="abs connect-card booking">
    <p class="eyebrow">Book &amp; Connect</p>
    <h2><span class="hl">Booking</span> should feel simple.</h2>
    <p>If you are curious about Kavenda®, want to enquire about movement sessions, or would like to ask a question...</p>
    <a class="btn btn-primary" href="#">Book a Session</a>
  </div>
  <div class="abs connect-card newsletter">
    <p class="eyebrow">Newsletter</p>
    <h2><span class="hl">Occasional</span> updates, not endless emails.</h2>
    <p>Hear about upcoming workshops, retreats, teacher trainings and new projects.</p>
    <div class="email-field">Your email address</div>
    <a class="btn btn-primary" href="#">Join The Mailing List</a>
  </div>
</section>

<footer class="site-footer">
  <div class="abs footer-brand"><span class="brand-dot" style="width:34px;height:34px"></span><span class="brand-name">Liesbet Oonwerk</span></div>
  <p class="abs footer-tag">Helping people feel more at home in their bodies through touch, movement, and education.</p>

  <div class="abs fcol" style="left:443px">
    <h4>EXPLORE</h4>
    <a href="#">Home</a><a href="#">Kavenda</a><a href="#">Movement</a><a href="#">Events</a><a href="#">Work With Me</a>
  </div>
  <div class="abs fcol" style="left:634px">
    <h4>INFORMATION</h4>
    <a href="#">About Liesbet</a><a href="#">Testimonials</a><a href="#">Pricing</a><a href="#">FAQ</a><a href="#">Contact</a>
  </div>
  <div class="abs fcol" style="left:843px">
    <h4>GET IN TOUCH</h4>
    <div class="contact-item"><svg width="16" height="16" viewBox="0 0 14 14" fill="#c9694a"><path d="M7 13s4.5-4.2 4.5-7.5a4.5 4.5 0 0 0-9 0C2.5 8.8 7 13 7 13z"/><circle cx="7" cy="5.5" r="1.6" fill="#e3d5c4"/></svg><span>Based in Leiden, the Netherlands<br>Working in English, Dutch, and French</span></div>
    <div class="contact-item"><svg width="16" height="16" viewBox="0 0 16 16" fill="#c9694a"><path d="M3 1.5h3l1.2 3.2-1.8 1.2a8 8 0 0 0 4.7 4.7l1.2-1.8 3.2 1.2v3a1.5 1.5 0 0 1-1.6 1.5A13 13 0 0 1 1.5 3.1 1.5 1.5 0 0 1 3 1.5z"/></svg><span>+31 6 0000 4821</span></div>
    <div class="contact-item"><svg width="16" height="16" viewBox="0 0 16 16" fill="none" stroke="#c9694a" stroke-width="1.5"><rect x="1.5" y="3" width="13" height="10" rx="1"/><path d="M1.5 4l6.5 5 6.5-5"/></svg><span>hello@liesbetoonwerk.com</span></div>
  </div>

  <div class="abs footer-base">
    <span>© 2026 Liesbet Oonwerk. All rights reserved.</span>
    <span>Kavenda® is a registered trademark of the Kaven Institute of Structural Integration.</span>
  </div>
</footer>

</body>
</html>
```